Real Estate For Sale Sign

I need to design a for sale sign. It needs to include The following information
Logo: Attached
Name: Corinne Vasquel,
Company Name: Gilded Harbor Real Estate,
Phone Number: 503-841-2096
BRE Licence Number 04817359 (Can Be small)
Sign size 24x30

I am not sure about including my website but I would like to see options with it. www.gildedharbor-example.com
Updates

Target Market(s)

Potential Buyers or Sellers of Real Estate. Must be easy to read.

Industry/Entity Type

Real Estate

Requirements
Must have
• I want it to feel luxurious and sharp.

```html
<!DOCTYPE html>
<html lang="en">
<head>
<meta charset="utf-8">
<title>Gilded Harbor Real Estate – For Sale Sign</title>
<link rel="stylesheet" href="https://fonts.googleapis.com/css2?family=Cinzel:wght@400;500&family=Arimo:wght@400;700&display=swap">
<style>
  :root {
    --page: #ffffff;
    --sign-top: #ffffff;
    --band: #33a3f2;
    --brand: #1f56c4;
    --ring: #3fb4ea;
    --ink-light: #ffffff;
    --ink-dark: #0c0c14;
    --edge: #cfd3d6;
  }
  * { margin: 0; padding: 0; box-sizing: border-box; }
  html, body {
    width: 1200px; height: 1000px; overflow: hidden;
    background: var(--page);
  }
  .sign {
    position: absolute; left: 0; top: 98px;
    width: 1200px; height: 804px;
    border-top: 2px solid var(--edge);
    border-bottom: 1px solid var(--edge);
    background: var(--sign-top);
    overflow: hidden;
  }
  .brand {
    position: absolute; left: 0; top: 0; width: 1200px; height: 382px;
  }
  .brand-mark {
    position: absolute; left: 108px; top: 52px;
  }
  .brand-name {
    position: absolute; left: 432px; top: 135px;
    font-family: "Cinzel", serif; font-weight: 500;
    color: var(--brand); text-align: center;
  }
  .brand-name .main { display: block; font-size: 62px; letter-spacing: 1px; line-height: 1; }
  .brand-name .sub { display: block; font-size: 34px; letter-spacing: 10px; margin-top: 20px; line-height: 1; }
  .band {
    position: absolute; left: 0; top: 382px; width: 1200px; height: 422px;
    background: var(--band);
  }
  .line {
    position: absolute; left: 0; width: 1200px; text-align: center;
    font-family: "Cinzel", serif; font-weight: 400;
    color: var(--ink-light); line-height: 1;
  }
  .line .dark { color: var(--ink-dark); }
  .agent-name { top: 56px; font-size: 60px; letter-spacing: 2px; padding-left: 30px; }
  .company { top: 148px; font-size: 50px; letter-spacing: 2px; }
  .phone { top: 226px; font-size: 68px; letter-spacing: 2px; padding-right: 20px; }
  .website {
    position: absolute; left: 24px; bottom: 20px;
    font-family: "Arimo", sans-serif; font-weight: 700; font-size: 15px;
    letter-spacing: 4px; color: var(--ink-light); text-transform: uppercase;
  }
  .licence {
    position: absolute; right: 30px; bottom: 16px;
    font-family: "Arimo", sans-serif; font-weight: 400; font-size: 26px;
    letter-spacing: 1px; color: var(--ink-dark);
  }
</style>
</head>
<body>
  <div class="sign">
    <header class="brand">
      <svg class="brand-mark" width="300" height="300" viewBox="0 0 300 300" aria-hidden="true">
        <circle cx="150" cy="150" r="140" fill="none" stroke="var(--ring)" stroke-width="8"/>
      </svg>
      <div class="brand-name">
        <span class="main">GILDED HARBOR</span>
        <span class="sub">REAL ESTATE</span>
      </div>
    </header>
    <section class="band">
      <p class="line agent-name">CORINNE <span class="dark">VASQUEL</span></p>
      <p class="line company">GILDED <span class="dark">HARBOR</span> REAL ESTATE</p>
      <p class="line phone">503-841-2096</p>
      <p class="website">www.gildedharbor-example.com</p>
      <p class="licence">BRE Licence Number 04817359</p>
    </section>
  </div>
</body>
</html>
```